Bref créative
Business Card and Stationary Design
Brevard Advisory Ltd.
Professional
Duncan Morvell
82 Pine Terrace SW
Calgary, AB T3K 6B9
duncan@brevardadvisory.example
www.brevardadvisory.example
I would like a design that includes some color.
I very much prefer the text to be very readable (clear, large).
I would like the back of the card to include the logo and some color.
Brevard Advisory Ltd. logo. AI format.

```html
<!DOCTYPE html>
<html lang="en">
<head>
<meta charset="utf-8">
<title>Brevard Advisory Ltd. — Stationery Set</title>
<link rel="stylesheet" href="https://fonts.googleapis.com/css2?family=Montserrat:wght@700;800&family=Open+Sans:wght@400;600&display=swap">
<style>
  :root {
    --navy: #163a72;
    --navy-deep: #0d2550;
    --blue: #2a5ea8;
    --paper: #ffffff;
    --paper-shade: #eef1f5;
    --ink: #3b3f46;
    --ink-soft: #7a808a;
    --faint: #e6e9ee;
    --backdrop: #d9dadb;
  }
  * { margin: 0; padding: 0; box-sizing: border-box; }
  html, body { width: 1200px; height: 583px; overflow: hidden; }
  body {
    background: var(--backdrop);
    font-family: "Open Sans", Arial, sans-serif;
    color: var(--ink);
    position: relative;
  }
  .piece {
    position: absolute;
    background: var(--paper);
    overflow: hidden;
    box-shadow: 0 2px 6px rgba(0,0,0,.22);
  }
  .piece > svg.shape {
    position: absolute; inset: 0; width: 100%; height: 100%;
  }
  .brand {
    position: absolute;
    display: flex; align-items: center; gap: 4px;
    font-family: "Montserrat", Arial, sans-serif;
    font-weight: 800;
    color: var(--navy);
    white-space: nowrap;
    letter-spacing: .2px;
  }
  .brand .dot {
    border-radius: 50%;
    background: var(--navy);
    flex: none;
  }
  .brand.on-dark { color: var(--paper); }
  .brand.on-dark .dot { background: var(--paper); }
  .contact {
    position: absolute;
    font-size: 4.6px; line-height: 1.45;
    color: var(--ink-soft);
    white-space: nowrap;
  }
  .contact .ico {
    display: inline-block; width: 4px; height: 4px; border-radius: 50%;
    background: var(--navy); margin-right: 2px; vertical-align: middle;
  }
  .watermark {
    position: absolute; border-radius: 50%;
    border: 6px solid var(--faint);
  }

  /* business card front */
  .card-front { left: 53px; top: 24px; width: 175px; height: 108px; }
  .card-front .brand { left: 10px; top: 12px; font-size: 9px; }
  .card-front .brand .dot { width: 12px; height: 12px; }
  .card-front .person {
    position: absolute; left: 12px; top: 44px;
    font-weight: 600; font-size: 6.5px; color: var(--navy);
  }
  .card-front .contact { left: 12px; top: 56px; font-size: 4.8px; }

  /* business card backs */
  .card-back {
    top: 144px; height: 103px;
    background: linear-gradient(135deg, var(--blue), var(--navy-deep));
  }
  .card-back.one { left: 53px; width: 156px; }
  .card-back.two { left: 221px; width: 151px; }
  .card-back .brand { left: 14px; top: 34px; font-size: 9px; }
  .card-back .brand .dot { width: 12px; height: 12px; }
  .card-back .badge {
    position: absolute; left: 50%; top: 38px; transform: translateX(-50%);
    width: 24px; height: 24px; border-radius: 50%; background: var(--paper);
  }
  .card-back .web {
    position: absolute; left: 0; right: 0; top: 74px; text-align: center;
    font-size: 5px; color: var(--paper);
  }

  /* compliment slip */
  .slip { left: 125px; top: 271px; width: 242px; height: 101px; }
  .slip .brand { left: 12px; top: 10px; font-size: 9px; }
  .slip .brand .dot { width: 12px; height: 12px; }
  .slip .contact { left: 14px; top: 28px; }
  .slip .watermark { left: 100px; top: 40px; width: 44px; height: 44px; }

  /* DL envelope front */
  .envelope-front { left: 108px; top: 408px; width: 257px; height: 139px; }
  .envelope-front .brand { left: 12px; top: 10px; font-size: 9px; }
  .envelope-front .brand .dot { width: 12px; height: 12px; }
  .envelope-front .contact { left: 14px; top: 27px; }

  /* letterheads */
  .letterhead { top: 43px; height: 329px; }
  .letterhead.primary { left: 396px; width: 240px; }
  .letterhead.secondary { left: 653px; width: 230px; }
  .letterhead .brand { left: 12px; top: 23px; font-size: 8px; gap: 3px; }
  .letterhead .brand .dot { width: 11px; height: 11px; }
  .letterhead .contact { left: 142px; top: 22px; font-size: 4.4px; }
  .letterhead .watermark { left: 50%; top: 250px; width: 56px; height: 56px; transform: translateX(-50%); }

  .letterhead.form { left: 907px; top: 43px; width: 226px; height: 341px; }
  .form .brand { left: 10px; top: 10px; font-size: 8px; }
  .form .contact { left: 140px; top: 9px; }
  .form .fields { position: absolute; left: 14px; top: 48px; right: 14px; }
  .form .field {
    display: flex; align-items: flex-end; gap: 4px; height: 9px;
    font-size: 4.6px; color: var(--ink);
  }
  .form .field .rule { flex: 1; border-bottom: .6px solid #b9bdc4; }
  .form .watermark { left: 50%; top: 252px; width: 56px; height: 56px; transform: translateX(-50%); }

  /* C4 envelope front */
  .envelope-large { left: 379px; top: 403px; width: 245px; height: 154px; }
  .envelope-large .brand { left: 12px; top: 10px; font-size: 9px; }
  .envelope-large .brand .dot { width: 12px; height: 12px; }
  .envelope-large .contact { left: 14px; top: 27px; }
  .envelope-large .watermark { left: 160px; top: 72px; width: 46px; height: 46px; }

  /* envelope backs */
  .envelope-back { top: 391px; height: 178px; background: var(--paper-shade); }
  .envelope-back.one { left: 641px; width: 247px; }
  .envelope-back.two { left: 907px; width: 226px; }
  .envelope-back .brand { left: 50%; top: 24px; transform: translateX(-50%); font-size: 8px; }
  .envelope-back .brand .dot { width: 11px; height: 11px; }
  .envelope-back .badge {
    position: absolute; left: 50%; top: 30px; transform: translateX(-50%);
    width: 22px; height: 22px; border-radius: 50%; background: var(--paper);
  }
</style>
</head>
<body>

<svg width="0" height="0" style="position:absolute">
  <defs>
    <linearGradient id="band" x1="0" y1="0" x2="1" y2="1">
      <stop offset="0" stop-color="#2a5ea8"/>
      <stop offset="1" stop-color="#0d2550"/>
    </linearGradient>
  </defs>
</svg>

<!-- Business card, front -->
<section class="piece card-front">
  <svg class="shape" viewBox="0 0 175 108" preserveAspectRatio="none">
    <path d="M95 0 H175 V40 C160 18 130 6 95 0 Z" fill="url(#band)"/>
    <path d="M0 100 C60 92 120 94 175 86 V108 H0 Z" fill="url(#band)"/>
  </svg>
  <div class="brand"><span class="dot"></span>Brevard Advisory Ltd.</div>
  <div class="person">Duncan Morvell</div>
  <div class="contact">
    <div><span class="ico"></span>82 Pine Terrace SW, Calgary, AB T3K 6B9</div>
    <div><span class="ico"></span>duncan@brevardadvisory.example</div>
    <div><span class="ico"></span>www.brevardadvisory.example</div>
  </div>
</section>

<!-- Business card, backs -->
<section class="piece card-back one">
  <div class="brand on-dark"><span class="dot"></span>Brevard Advisory Ltd.</div>
</section>
<section class="piece card-back two">
  <div class="badge"></div>
  <div class="web">www.brevardadvisory.example</div>
</section>

<!-- Compliment slip -->
<section class="piece slip">
  <svg class="shape" viewBox="0 0 242 101" preserveAspectRatio="none">
    <path d="M120 0 H242 V34 C210 10 170 2 120 0 Z" fill="url(#band)"/>
  </svg>
  <div class="brand"><span class="dot"></span>Brevard Advisory Ltd.</div>
  <div class="contact">
    <div><span class="ico"></span>82 Pine Terrace SW, Calgary, AB T3K 6B9</div>
    <div><span class="ico"></span>www.brevardadvisory.example</div>
  </div>
  <div class="watermark"></div>
</section>

<!-- DL envelope -->
<section class="piece envelope-front">
  <svg class="shape" viewBox="0 0 257 139" preserveAspectRatio="none">
    <path d="M130 0 H257 V34 C225 10 180 2 130 0 Z" fill="url(#band)"/>
  </svg>
  <div class="brand"><span class="dot"></span>Brevard Advisory Ltd.</div>
  <div class="contact">
    <div>82 Pine Terrace SW</div>
    <div>Calgary, AB T3K 6B9</div>
  </div>
</section>

<!-- Letterhead, primary -->
<section class="piece letterhead primary">
  <svg class="shape" viewBox="0 0 240 329" preserveAspectRatio="none">
    <path d="M0 0 H240 V16 C170 8 80 6 0 12 Z" fill="url(#band)"/>
    <path d="M170 0 H240 V46 C225 22 200 8 170 0 Z" fill="url(#band)"/>
  </svg>
  <div class="brand"><span class="dot"></span>Brevard Advisory Ltd.</div>
  <div class="contact">
    <div><span class="ico"></span>82 Pine Terrace SW</div>
    <div><span class="ico"></span>Calgary, AB T3K 6B9</div>
  </div>
  <div class="watermark"></div>
</section>

<!-- Letterhead, secondary -->
<section class="piece letterhead secondary">
  <svg class="shape" viewBox="0 0 230 329" preserveAspectRatio="none">
    <path d="M0 0 H230 V8 C150 4 70 4 0 8 Z" fill="url(#band)"/>
    <path d="M0 329 V318 C80 312 160 314 230 306 V329 Z" fill="url(#band)"/>
  </svg>
  <div class="brand"><span class="dot"></span>Brevard Advisory Ltd.</div>
  <div class="contact">
    <div><span class="ico"></span>82 Pine Terrace SW</div>
    <div><span class="ico"></span>Calgary, AB T3K 6B9</div>
  </div>
  <div class="watermark"></div>
</section>

<!-- Letterhead, form -->
<section class="piece letterhead form">
  <svg class="shape" viewBox="0 0 226 341" preserveAspectRatio="none">
    <path d="M0 341 V326 C70 316 150 318 226 300 V341 Z" fill="url(#band)"/>
    <path d="M0 322 C70 312 150 314 226 296" fill="none" stroke="#2a5ea8" stroke-width="1"/>
  </svg>
  <div class="brand"><span class="dot"></span>Brevard Advisory Ltd.</div>
  <div class="contact">
    <div><span class="ico"></span>82 Pine Terrace SW</div>
    <div><span class="ico"></span>Calgary, AB T3K 6B9</div>
  </div>
  <div class="fields">
    <div class="field">To:<span class="rule"></span></div>
    <div class="field">From:<span class="rule"></span></div>
    <div class="field">Date:<span class="rule"></span></div>
    <div class="field">Subject:<span class="rule"></span></div>
    <div class="field">Pages:<span class="rule"></span></div>
  </div>
  <div class="watermark"></div>
</section>

<!-- C4 envelope -->
<section class="piece envelope-large">
  <svg class="shape" viewBox="0 0 245 154" preserveAspectRatio="none">
    <path d="M0 0 H245 V6 C160 3 80 3 0 6 Z" fill="url(#band)"/>
  </svg>
  <div class="brand"><span class="dot"></span>Brevard Advisory Ltd.</div>
  <div class="contact">
    <div>82 Pine Terrace SW</div>
    <div>Calgary, AB T3K 6B9</div>
  </div>
  <div class="watermark"></div>
</section>

<!-- Envelope backs -->
<section class="piece envelope-back one">
  <svg class="shape" viewBox="0 0 247 178" preserveAspectRatio="none">
    <path d="M0 0 H247 V10 C190 30 150 60 123 68 C96 60 57 30 0 10 Z" fill="url(#band)"/>
  </svg>
  <div class="brand on-dark"><span class="dot"></span>Brevard Advisory Ltd.</div>
</section>
<section class="piece envelope-back two">
  <svg class="shape" viewBox="0 0 226 178" preserveAspectRatio="none">
    <path d="M0 0 H226 V10 C175 36 140 66 113 72 C86 66 51 36 0 10 Z" fill="url(#band)"/>
  </svg>
  <div class="badge"></div>
</section>

</body>
</html>
```